We need a web design for an existing company that has been in business for 16 years, based in the Dallas-Ft. Worth, Texas area. We also just received a new logo from PixelForge that we want to incorporate with the site. The site should have a professional look and feel that will grow with us. We need the website to include a holding place for project photos that will demonstrate a "before and after" view of our work. We will upload photos of our work once the site is designed. Vestry Building Maintenance provides the following services: Pressure Washing, Parking Lot Striping, and Janitorial Services for commercial businesses of all types. We also provide exterior and Interior commercial and residential painting services. We are insured and use bio-friendly cleaners. The site will also need a "Request a Quote" section where people can submit their contact information for a bid from us. This would be just shooting off an email to us once they click submit. We want the site to be professional, clean and simple but with a slick design!
Target Market(s)
Commercial businesses
Industry/Entity Type
Residential
Number of Pages Required
4 page
Look and feel

```html
<!DOCTYPE html>
<html lang="en">
<head>
<meta charset="utf-8">
<title>Vestry Building Maintenance</title>
<link href="https://fonts.googleapis.com/css2?family=Roboto:wght@400;500;700&family=Ubuntu:wght@400;500&display=swap" rel="stylesheet">
<style>
:root{
  --green:#7cb518;
  --green-dark:#5e9a0c;
  --navy:#0f2748;
  --navy-deep:#0a1a33;
  --band:#1d3d66;
  --orange:#f7941d;
  --orange-dark:#ef7b00;
  --ink:#444;
  --muted:#666;
  --footer-light:#ececec;
  --footer-dark:#222;
  --white:#fff;
}
*{box-sizing:border-box;margin:0;padding:0}
html,body{width:882px;height:1200px;overflow:hidden}
body{position:relative;background:var(--white);font-family:'Roboto',sans-serif;color:var(--ink)}
.abs{position:absolute}
.logo{left:95px;top:18px;display:flex;align-items:center;gap:6px}
.logo-name{font-family:'Roboto',sans-serif;font-weight:500;font-size:26px;color:#333;letter-spacing:1px}
.logo-mark{width:12px;height:12px;background:var(--green)}
.logo-tag{left:95px;top:44px;font-size:8px;color:var(--green-dark);letter-spacing:1px}
.phone{right:97px;top:24px;display:flex;align-items:center;gap:6px;font-size:16px;color:#777}
.nav{left:95px;top:65px;width:691px;height:44px;background:linear-gradient(#86c41f,#65a30d);display:flex}
.nav a{color:var(--white);text-decoration:none;font-size:11.5px;display:flex;align-items:center;padding:0 16px;border-right:1px solid rgba(255,255,255,.25)}
.nav a.active{background:linear-gradient(#555,#222);width:68px;justify-content:center}
.band{left:0;top:333px;width:882px;height:329px;background:linear-gradient(180deg,#27507f 0%,#1b3a62 60%,#15304f 100%)}
.hero{left:96px;top:109px;width:479px;height:293px;background:linear-gradient(180deg,#8c9296 0%,#6f7a72 45%,#4f6a3a 100%)}
.hero-title{left:119px;top:283px;color:var(--white);font-size:15px;font-weight:500}
.hero-title span{color:var(--green)}
.hero-sub{left:120px;top:303px;color:var(--white);font-size:11px}
.dots{left:515px;top:383px;display:flex;gap:5px}
.dots i{width:8px;height:8px;border-radius:50%;background:rgba(255,255,255,.45)}
.dots i:last-child{background:var(--white)}
.quote{left:575px;top:109px;width:210px;height:293px;background:#000;padding:12px 21px}
.quote h2{color:var(--white);font-size:15px;font-weight:500;text-align:center;margin-bottom:10px}
.field{background:var(--white);height:27px;margin-bottom:8px;font-size:8px;color:#333;padding:9px 7px}
.field.msg{height:40px;padding-top:6px}
.submit{margin-top:12px;height:38px;background:linear-gradient(#ffa31a,var(--orange-dark));color:var(--white);font-weight:700;font-size:14px;text-align:center;line-height:38px;border-radius:2px}
.services-title{left:95px;top:420px;color:var(--white);font-size:15.5px}
.card{top:455px;width:162px;height:192px;background:rgba(8,22,44,.85);padding:16px 14px}
.card h3{color:var(--white);font-size:11px;font-weight:500;margin-bottom:9px}
.card .photo{width:132px;height:71px;border:2px solid var(--white);margin-bottom:9px}
.card li{list-style:none;color:var(--white);font-size:7.5px;margin-bottom:11px;padding-left:14px;position:relative}
.card li::before{content:"";position:absolute;left:2px;top:2px;border-left:4px solid #aaa;border-top:3px solid transparent;border-bottom:3px solid transparent}
.welcome-img{left:93px;top:685px;width:207px;height:140px;border:3px solid var(--white);box-shadow:0 0 4px rgba(0,0,0,.35);background:linear-gradient(135deg,#3a3f44,#7b8a8e 60%,#2d3236)}
.welcome-h{left:316px;top:685px;font-size:14.5px;color:#333}
.welcome-h span{color:var(--green-dark);margin-left:4px}
.welcome-p{left:317px;top:710px;width:469px;font-size:9.4px;line-height:16.8px;color:#555;text-align:justify}
.cta{top:854px;width:221px;height:86px;background:var(--navy);box-shadow:0 3px 4px rgba(0,0,0,.3);display:flex;align-items:center}
.cta-icon{width:52px;height:52px;margin:0 10px 0 26px;background:linear-gradient(#ffa31a,var(--orange-dark));border-radius:3px;display:flex;align-items:center;justify-content:center}
.cta-big{font-family:'Ubuntu',sans-serif;font-size:23px;color:var(--green)}
.cta-small{font-family:'Ubuntu',sans-serif;font-size:12px;color:var(--white)}
.cta-mid{flex-direction:column;justify-content:center;text-align:center;color:var(--white);font-size:9px;line-height:15px}
.cta-btn{margin-top:6px;background:linear-gradient(#ffa31a,var(--orange-dark));color:var(--white);font-weight:700;font-size:8.5px;padding:6px 14px}
.cta-building{width:60px;height:64px;margin:0 8px 0 10px;background:linear-gradient(135deg,#d7e3ee,#6f8aa5)}
.cta-name{font-family:'Ubuntu',sans-serif;font-size:18px;line-height:24px;color:var(--white)}
.cta-name span{color:var(--green)}
.footer-top{left:0;top:955px;width:882px;height:150px;background:var(--footer-light)}
.fcol{top:986px}
.fcol h4{color:var(--green-dark);font-size:11.5px;font-weight:500;margin-bottom:18px}
.fcol p{font-size:9.6px;color:#444;margin-bottom:10px}
.footer-bottom{left:0;top:1105px;width:882px;height:95px;background:var(--footer-dark)}
.flinks{left:95px;top:1136px;color:var(--white);font-size:9.6px}
.copy{left:95px;top:1156px;color:var(--white);font-size:11.5px}
.social{right:97px;top:1141px;display:flex;gap:9px}
.social i{width:25px;height:25px;background:#4a5563;border-radius:2px}
</style>
</head>
<body>
<header>
  <div class="abs logo"><span class="logo-name">VESTRY</span><span class="logo-mark"></span></div>
  <div class="abs logo-tag">building maintenance</div>
  <div class="abs phone">
    <svg width="18" height="18" viewBox="0 0 18 18"><circle cx="9" cy="9" r="8" fill="none" stroke="#7cb518" stroke-width="1.6"/><path d="M6 5l2 0 1 2.5-1.2 1a6 6 0 0 0 2.7 2.7l1-1.2 2.5 1v2a1 1 0 0 1-1 1A8 8 0 0 1 5 6a1 1 0 0 1 1-1z" fill="#7cb518"/></svg>
    (555) 014-2291
  </div>
  <nav class="abs nav">
    <a class="active">HOME</a><a>ABOUT US</a><a>SERVICES</a><a>OFFER</a><a>MAINTANCE</a><a>TESTIMONIALS</a><a>NEWS</a><a style="border:0">CONTACTS</a>
  </nav>
</header>

<div class="abs band"></div>
<div class="abs hero" role="img" aria-label="Photo of a two-storey suburban house with grey siding and a green lawn"></div>
<div class="abs hero-title">VESTRY BUILDING <span>MAINTENANCE</span></div>
<div class="abs hero-sub">Lorem Ipsum is simply dummy text of the printing</div>
<div class="abs dots"><i></i><i></i><i></i><i></i></div>

<form class="abs quote">
  <h2>REQUEST A QUOTE</h2>
  <div class="field">Name :</div>
  <div class="field">Email id :</div>
  <div class="field">Phone :</div>
  <div class="field">Searvice :</div>
  <div class="field msg">Message :</div>
  <div class="submit">SUBMIT</div>
</form>

<h2 class="abs services-title" style="font-weight:400">VESTRY BUILDING MAINTENANCE PROVIDES THE FOLLOWING SERVICES</h2>

<section class="abs card" style="left:95px">
  <h3>PRESSURE WASHING</h3>
  <div class="photo" role="img" aria-label="Worker pressure washing a wooden porch" style="background:linear-gradient(#cfd6dc,#8a6e52)"></div>
  <ul><li>Lorem ipsum dolor sit amet</li><li>Sed do eiusmod tempor incididunt</li><li>Duis aute irure dolor in</li></ul>
</section>
<section class="abs card" style="left:272px">
  <h3>PARKING LOT STRIPING</h3>
  <div class="photo" role="img" aria-label="Freshly painted accessible parking bay on asphalt" style="background:linear-gradient(135deg,#3b3b3b,#4a6fb5 50%,#3b3b3b)"></div>
  <ul><li>Lorem ipsum dolor sit amet</li><li>Sed do eiusmod tempor incididunt</li><li>Duis aute irure dolor in</li></ul>
</section>
<section class="abs card" style="left:448px">
  <h3>JANITORIAL SERVICES</h3>
  <div class="photo" role="img" aria-label="Cleaner wiping a white washroom wall" style="background:linear-gradient(90deg,#e8e8e8,#bdbdbd)"></div>
  <ul><li>Lorem ipsum dolor sit amet</li><li>Sed do eiusmod tempor incididunt</li><li>Duis aute irure dolor in</li></ul>
</section>
<section class="abs card" style="left:624px">
  <h3>BEFORE &amp; AFTER</h3>
  <div class="photo" role="img" aria-label="Before and after view of a building facade" style="background:linear-gradient(90deg,#9a9a9a 50%,#c9a98a 50%)"></div>
  <ul><li>Lorem ipsum dolor sit amet</li><li>Sed do eiusmod tempor incididunt</li><li>Duis aute irure dolor in</li></ul>
</section>

<div class="abs welcome-img" role="img" aria-label="Window cleaner holding a squeegee and spray bottle"></div>
<h2 class="abs welcome-h" style="font-weight:400">WELCOME TO <span>VESTRY BUILDING MAINTENANCE</span></h2>
<p class="abs welcome-p">Lorem ipsum dolor sit amet, consectetur adipisicing elit, sed do eiusmod tempor incididunt ut labore et dolore magna aliqua. Ut enim ad minim veniam, quis nostrud exercitation ullamco laboris nisi ut aliquip ex ea commodo consequat. Duis aute irure dolor in reprehenderit in voluptate velit esse cillum dolore eu fugiat nulla pariatur. Excepteur sint occaecat cupidatat non proident, sunt in culpa qui officia deserunt mollit anim id est laborum.adipisicing elit, sed do eiusmod tempor incididunt .</p>

<div class="abs cta" style="left:95px">
  <div class="cta-icon"><svg width="34" height="24" viewBox="0 0 34 24"><rect x="1" y="1" width="32" height="22" fill="#fff" stroke="#ddd"/><path d="M1 1l16 12L33 1" fill="none" stroke="#ccc" stroke-width="1.5"/></svg></div>
  <div><div class="cta-big">Contact Us</div><div class="cta-small">For a free estimate</div></div>
</div>
<div class="abs cta cta-mid" style="left:330px">
  <div>laudantium, totam rem aperiam, eaque ipsa<br>quae ab illo inventore veritatis et</div>
  <div class="cta-btn">GET A FREE QUOTE</div>
</div>
<div class="abs cta" style="left:565px">
  <div class="cta-building" role="img" aria-label="Office building graphic"></div>
  <div class="cta-name">Vestry Building<br><span>Maintenance</span></div>
</div>

<footer>
  <div class="abs footer-top"></div>
  <div class="abs fcol" style="left:96px"><h4>COMPANY</h4><p>About us</p><p>Services</p><p>Presentation</p></div>
  <div class="abs fcol" style="left:227px"><h4>SPECIALISTS</h4><p>Commercial</p><p>Residential</p><p>Luxury</p></div>
  <div class="abs fcol" style="left:361px"><h4>ADVICE</h4><p>FAQs</p><p>Support</p></div>
  <div class="abs fcol" style="left:477px"><h4>AGENCIES</h4><p>Sign Up</p><p>Forums</p><p>Promotions</p></div>
  <div class="abs fcol" style="left:604px"><h4>CONTACT US</h4><p>412 Cedar Hollow Lane, Arlington, TX 76010</p><p>Phone: +1 555 018 7720</p><p>E-mail: hello@vestrybm.example</p></div>
  <div class="abs footer-bottom"></div>
  <div class="abs flinks">About &nbsp;|&nbsp; Disclaimer &nbsp;|&nbsp; Contact &nbsp;|&nbsp; Sitemap &nbsp;|&nbsp; Hosted Solutions Partner</div>
  <div class="abs copy">Copyright © 2015 &nbsp;All Rights</div>
  <div class="abs social"><i></i><i></i><i></i><i></i></div>
</footer>
</body>
</html>
```